Simple one page Wordpress website

We need a quick turnaround single page wordpress website.
The design needs to be very simple and clean.
We already have some design assets (logos and colours etc) and some draft copy for the page.

We need all the files for us to be able to create a wordpress site. We can do this ourselves and we will host it.

```html
<!DOCTYPE html>
<html lang="en">
<head>
<meta charset="utf-8">
<title>VetNova – Turnkey Initial Veterinary Deployment</title>
<link rel="stylesheet" href="https://fonts.googleapis.com/css2?family=Poppins:wght@400;500;600&family=Open+Sans:wght@400;600&display=swap">
<style>
:root{
  --blue:#2b7bbb;
  --blue-dark:#1d5f94;
  --green:#8cba3c;
  --ink:#1f2328;
  --text:#4a4f55;
  --muted:#7b8188;
  --band:#f2f3f5;
  --line:#d9dde2;
  --white:#ffffff;
}
*{box-sizing:border-box;margin:0;padding:0}
html,body{width:1200px;height:3468px;overflow:hidden;background:var(--white)}
body{font-family:"Open Sans",Arial,sans-serif;color:var(--text);position:relative}
h1,h2,h3,.brand{font-family:"Poppins",Arial,sans-serif;color:var(--ink);font-weight:500}
.section{position:absolute;left:0;width:1200px}
.brand{display:flex;align-items:center;gap:10px;font-size:30px;font-weight:600;color:var(--blue-dark);letter-spacing:1px}
.brand-mark{width:18px;height:18px;background:var(--green)}

/* header */
.site-header{top:0;height:72px;display:flex;align-items:center;justify-content:space-between;padding:0 80px}
.nav{display:flex;align-items:center;gap:26px;font-size:15px;color:var(--ink)}
.nav .active{color:var(--blue)}
.btn{display:inline-block;border-radius:20px;padding:8px 22px;font-size:14px;font-weight:600}
.btn-solid{background:var(--blue);color:var(--white)}
.btn-outline{border:1.5px solid var(--blue);color:var(--blue);padding:6.5px 20px}

/* hero */
.hero{top:72px;height:568px}
.hero-copy{position:absolute;left:80px;top:100px;width:430px}
.hero h1{font-size:40px;line-height:1.28}
.hero h1 span{color:var(--blue)}
.hero p{margin-top:22px;font-size:15px;line-height:1.6;width:300px}
.hero .btn{margin-top:22px;border-radius:6px}
.hero-points{list-style:none;display:grid;grid-template-columns:auto auto;gap:10px 36px;margin-top:22px;font-size:14px;color:var(--ink)}
.hero-points li{display:flex;align-items:center;gap:8px}
.dot{width:11px;height:11px;border-radius:50%;background:var(--green);flex:none}
.hero-visual{position:absolute;left:530px;top:30px;width:650px;height:510px;border-radius:14px;background:linear-gradient(135deg,#e9eef4,#c9d3de 60%,#aab6c3)}

/* mission */
.mission{top:640px;height:340px;text-align:center}
.mission h2{margin-top:100px;font-size:34px}
.mission p{width:640px;margin:30px auto 0;font-size:17px;line-height:1.65;color:var(--text)}

/* capabilities */
.capabilities{top:980px;height:500px;background:var(--band)}
.capabilities h2{position:absolute;left:80px;top:120px;font-size:34px}
.capabilities ul{position:absolute;left:80px;top:200px;width:520px;list-style:none}
.capabilities li{display:flex;gap:14px;font-size:16px;line-height:1.6;margin-bottom:22px}
.capabilities .dot{margin-top:7px}
.cap-visual{position:absolute;left:660px;top:80px;width:460px;height:340px;border-radius:8px;background:linear-gradient(135deg,#1b3f66,#2b79b6 55%,#7fc0e6)}

/* deployment */
.deployment{top:1480px;height:700px}
.deploy-visual{position:absolute;left:0;top:40px;width:470px;height:360px;background:linear-gradient(135deg,#b7c5d4,#6b86a3 60%,#3f5a78)}
.deploy-note{position:absolute;left:180px;top:400px;width:290px;background:var(--white);padding:18px 20px;font-size:15px;line-height:1.55;color:var(--ink);box-shadow:0 6px 18px rgba(0,0,0,.08)}
.deploy-note a{color:var(--blue);text-decoration:none;font-weight:600}
.deploy-copy{position:absolute;left:600px;top:60px;width:520px}
.deploy-copy h2{font-size:34px;line-height:1.28}
.deploy-copy p{margin-top:24px;font-size:15px;line-height:1.6}
.deploy-copy ul{list-style:none;margin-top:20px}
.deploy-copy li{display:flex;align-items:center;gap:12px;font-size:15px;margin-bottom:17px}
.deploy-copy .dot{background:var(--blue);width:9px;height:9px}

/* background */
.background{top:2180px;height:700px;background:var(--band);text-align:center}
.background h2{margin-top:40px;font-size:34px}
.background .lead{margin-top:12px;font-size:17px}
.partners{position:absolute;left:80px;top:160px;display:flex;gap:40px}
.partner-card{width:500px;height:460px;background:var(--white);border:1px solid var(--line)}
.partner-card h3{background:var(--green);color:var(--white);font-size:16px;font-weight:600;padding:14px 10px}
.partner-card p{padding:34px 40px;font-size:15px;line-height:1.6}

/* team */
.team{top:2880px;height:480px;text-align:center}
.team h2{margin-top:60px;font-size:34px}
.team-row{position:absolute;left:0;top:160px;display:flex;gap:30px}
.member{position:relative;width:220px;height:300px;border-radius:6px;background:linear-gradient(180deg,#dfe5ec,#a9b6c4)}
.member.alt{background:linear-gradient(180deg,#e9e3dc,#b7a99a)}
.member-info{position:absolute;inset:0;border-radius:6px;background:rgba(43,123,187,.82);color:var(--white);padding:60px 18px;font-size:13px;line-height:1.5}
.member-info h3{color:var(--white);font-size:17px;margin-bottom:8px}

/* footer */
.site-footer{top:3360px;height:108px;border-top:1px solid var(--line);padding:0 80px}
.footer-row{display:flex;align-items:center;justify-content:space-between;height:60px}
.footer-row .info{font-size:16px;color:var(--ink)}
.footer-row .info b{color:var(--blue);font-weight:600}
.social{display:flex;gap:10px}
.social span{width:26px;height:26px;border-radius:4px;background:var(--blue)}
.copyright{font-size:14px;color:var(--muted);padding-top:14px}
</style>
</head>
<body>

<header class="section site-header">
  <div class="brand"><span class="brand-mark"></span>VetNova</div>
  <nav class="nav">
    <span class="active">Home</span><span>Mission</span><span>Capabilities</span><span>Team</span><span>Contact</span>
    <span class="btn btn-solid">Login</span><span class="btn btn-outline">Sign Up</span>
  </nav>
</header>

<section class="section hero">
  <div class="hero-copy">
    <h1><span>Turnkey</span> Initial Veterinary Deployment – Animal Health and Welfare Pathway</h1>
    <p>Lorem Ipsum is simply dummy text of the printing and typesetting industry.</p>
    <span class="btn btn-solid">Contact Us</span>
    <ul class="hero-points">
      <li><span class="dot"></span>Efficient Collection</li>
      <li><span class="dot"></span>Transmission</li>
      <li><span class="dot"></span>Secure Storage</li>
    </ul>
  </div>
  <div class="hero-visual" role="img" aria-label="Laptop and phone showing the platform dashboard"></div>
</section>

<section class="section mission">
  <h2>Our Mission</h2>
  <p>VetNova is deploying a Software as a Service (SaaS) platform to facilitate the efficient collection, transmission, secure storage and anonymised analysis of data integral to animal diagnostics.</p>
</section>

<section class="section capabilities">
  <h2>Capabilities</h2>
  <ul>
    <li><span class="dot"></span>Originally developed for the human market, the core platform has been deployed in the UK and Ireland and has been used to securely process nearly 3 million cases</li>
    <li><span class="dot"></span>The platform has been widely used by leading pharmacies, employers, the national health service and most of the UK's largest private sector laboratories</li>
  </ul>
  <div class="cap-visual" role="img" aria-label="Abstract digital data and laboratory imagery"></div>
</section>

<section class="section deployment">
  <div class="deploy-visual" role="img" aria-label="Person working with reports and charts on a laptop"></div>
  <div class="deploy-note">Interested parties seeking further information should contact us at <a>info@vetnova.com</a></div>
  <div class="deploy-copy">
    <h2>Turnkey Initial Veterinary Deployment – Animal Health and Welfare Pathway</h2>
    <p>VetNova is finalising the design of a bespoke platform to facilitate the collection and processing of data and tests for the Animal Health and Welfare Pathway. Key elements include:</p>
    <ul>
      <li><span class="dot"></span>Facilitated data collection at the farm by vets</li>
      <li><span class="dot"></span>Secure and efficient processing of test samples by labs</li>
      <li><span class="dot"></span>Digital results reporting</li>
      <li><span class="dot"></span>Invoice support</li>
      <li><span class="dot"></span>Data analysis reporting</li>
    </ul>
  </div>
</section>

<section class="section background">
  <h2>Background</h2>
  <p class="lead">VetNova is a joint venture between:</p>
  <div class="partners">
    <article class="partner-card">
      <h3>Harrow Field Solutions Limited (HFS)</h3>
      <p>An innovative veterinary-led, close to market sustainable food research organisation. HFS brings together a team of highly experienced vets representing key opinion leaders within the livestock industry and additional technical support staff through its shareholder practice Elmbridge Veterinary Group, Yorkshire. Elmbridge is a 15 year old six centre veterinary group in North Yorkshire, focusing on livestock and equine. In turn Elmbridge is part of AgriVetNet, an independent grouping of 40+ Farm and Equine practices across the UK.</p>
    </article>
    <article class="partner-card">
      <h3>Tailored Assay Systems Limited (TAS)</h3>
      <p>A rapidly growing Software as a Service platform provider in the digital health market. TAS deploys its agile and collaborative software development process working in partnership with its clients, using the skills of both parties to build the best solutions as effectively and efficiently as possible. Its clients include some of the country's largest pharmacies, employers and laboratories.</p>
    </article>
  </div>
</section>

<section class="section team">
  <h2>The Team</h2>
  <div class="team-row">
    <div class="member" role="img" aria-label="Team member portrait"></div>
    <div class="member alt">
      <div class="member-info"><h3>Person 2</h3>Senior veterinary advisor with two decades of farm practice, leading our clinical data and welfare programme.</div>
    </div>
    <div class="member" role="img" aria-label="Team member portrait"></div>
    <div class="member alt" role="img" aria-label="Team member portrait"></div>
    <div class="member" role="img" aria-label="Team member portrait"></div>
  </div>
</section>

<footer class="section site-footer">
  <div class="footer-row">
    <div class="brand"><span class="brand-mark"></span>VetNova</div>
    <div class="info">Location : <b>Enter Location Here</b></div>
    <div class="info">Email : <b>info@vetnova.com</b></div>
    <div class="info">Call : <b>+01 23 456 789</b></div>
    <div class="social"><span></span><span></span><span></span></div>
  </div>
  <p class="copyright">Copyright 2022.VETNOVA.All right reserved.</p>
</footer>

</body>
</html>
```